The billboard should communicate confidence, energy and approachability while maintaining a professional, premium feel. Rather than relying on a standard agent photograph, property collage or crowded list of services, we would like an original creative idea that makes people look twice. This could involve a fun visual, clever headline, striking colour contrast or an unexpected real estate theme. The concept should feel positive and contemporary, with enough personality to become recognisable throughout the local community.

The key message should appeal to homeowners who are thinking about selling, preparing to sell or simply curious about the value of their property. Copy must be short, clear and conversational, supported by a direct call to action. The agent’s name, phone number and company branding should remain highly visible without competing with the main idea.

The finished billboard will measure 8.0 metres wide by 2.08 metres high (1224px x 324px), so the composition must suit a long landscape format. All important text and imagery should remain comfortably within safe margins and be legible from a distance. The design should avoid small writing, unnecessary detail and visual clutter.

The goal is to create a billboard that feels different from every other real estate sign in the area—something engaging, confident and easy to remember. It should build strong brand awareness, generate conversations and encourage local property owners to contact the agent when they are ready to make their next move. The concept should be adaptable for future campaigns, helping establish a consistent, distinctive and trusted local brand presence.

Target Market(s)

ages 30+

Industry/Entity Type

Real Estate

Requirements
Must have
• call Colin and phone number 0437 15 82 63
Nice to have
• Nice bright and yellow.. Exciting and grabbing

```html
<!DOCTYPE html>
<html lang="en">
<head>
<meta charset="utf-8">
<title>Thinking of Selling? – Billboard</title>
<link rel="stylesheet" href="https://fonts.googleapis.com/css2?family=Archivo+Black&family=Oswald:wght@500;600;700&family=Barlow+Condensed:ital,wght@0,700;0,800;1,800&display=swap">
<style>
  :root {
    --yellow: #FAD20A;
    --charcoal: #333234;
    --ink: #2F2E30;
    --white: #FFFFFF;
  }
  * { margin: 0; padding: 0; box-sizing: border-box; }
  html, body { width: 1200px; height: 312px; overflow: hidden; background: var(--charcoal); }
  .billboard { position: relative; width: 1200px; height: 312px; overflow: hidden; background: var(--yellow); }

  .hero-photo {
    position: absolute; left: 680px; top: 0; width: 520px; height: 227px;
    background:
      radial-gradient(ellipse at 45% 55%, rgba(255,214,140,0.55), transparent 60%),
      linear-gradient(180deg, #8FA3A8 0%, #9C8E6A 40%, #6F7A45 75%, #4E5A34 100%);
  }
  .hero-fade {
    position: absolute; left: 680px; top: 0; width: 140px; height: 227px;
    background: linear-gradient(90deg, var(--yellow) 0%, rgba(250,210,10,0.6) 45%, rgba(250,210,10,0) 100%);
  }

  .headline {
    position: absolute; left: 32px; top: 12px;
    font-family: "Archivo Black", sans-serif; color: var(--ink);
    font-size: 88px; line-height: 78px; letter-spacing: 1px;
  }
  .headline span { display: block; }
  .headline .line-two { margin-left: 0; }

  .subline {
    position: absolute; left: 38px; top: 182px;
    font-family: "Barlow Condensed", sans-serif; font-weight: 800;
    font-size: 33px; line-height: 1; color: var(--ink); letter-spacing: 0.3px;
  }
  .subline em { color: var(--white); font-style: italic; }

  .move-sign {
    position: absolute; left: 1010px; top: 42px; width: 172px; height: 144px;
    background: var(--charcoal); transform: rotate(2deg);
    font-family: "Oswald", sans-serif; font-weight: 600; color: var(--white);
    text-align: center; padding-top: 24px; line-height: 1;
  }
  .move-sign .small { display: block; font-size: 21px; }
  .move-sign .big { display: block; font-size: 44px; font-weight: 700; color: var(--yellow); margin: 2px 0 4px; }

  .contact-bar {
    position: absolute; left: 0; top: 227px; width: 1200px; height: 85px;
    background: var(--charcoal);
  }
  .phone-icon { position: absolute; left: 41px; top: 245px; width: 50px; height: 50px; }
  .agent-name {
    position: absolute; left: 104px; top: 250px;
    font-family: "Oswald", sans-serif; font-weight: 500; font-size: 31px; line-height: 40px;
    color: var(--white); letter-spacing: 0.2px;
  }
  .divider { position: absolute; left: 354px; top: 254px; width: 3px; height: 34px; background: var(--yellow); }
  .agent-phone {
    position: absolute; left: 373px; top: 248px;
    font-family: "Oswald", sans-serif; font-weight: 600; font-size: 36px; line-height: 44px;
    color: var(--yellow); letter-spacing: 0.5px;
  }
  .brand-name {
    position: absolute; right: 32px; top: 252px;
    font-family: "Oswald", sans-serif; font-weight: 700; font-size: 36px; line-height: 40px;
    color: var(--yellow); letter-spacing: 0.5px;
  }
</style>
</head>
<body>
<div class="billboard">
  <div class="hero-photo" role="img" aria-label="Photo of a dog in sunglasses riding in a yellow convertible in front of a lit family home at dusk"></div>
  <div class="hero-fade"></div>

  <h1 class="headline"><span>THINKING</span><span class="line-two">OF SELLING?</span></h1>
  <p class="subline">LET’S FIND OUT WHAT IT’S <em>REALLY</em> WORTH.</p>

  <div class="move-sign">
    <span class="small">YOUR NEXT</span>
    <span class="big">MOVE</span>
    <span class="small">STARTS HERE.</span>
  </div>

  <div class="contact-bar"></div>
  <svg class="phone-icon" viewBox="0 0 50 50" aria-hidden="true">
    <circle cx="25" cy="25" r="24" fill="#FAD20A"/>
    <path d="M18 13c1.5-1 3-.5 3.8 1l2 4c.6 1.2.2 2.4-.8 3.2l-1.4 1.1c1.2 2.6 3.2 4.7 5.8 6l1.1-1.4c.8-1 2.1-1.3 3.2-.8l4 2c1.5.8 2 2.3 1 3.8l-1.5 2.2c-1 1.4-2.8 2-4.4 1.5C22.6 33.6 16.4 27.4 14.4 19.2c-.4-1.6.1-3.3 1.5-4.4z" fill="#333234"/>
  </svg>
  <div class="agent-name">COLIN HARWOOD</div>
  <div class="divider"></div>
  <div class="agent-phone">0437 15 82 63</div>
  <div class="brand-name">DALE FORSYTH</div>
</div>
</body>
</html>
```